BrightFern Web Design Project

BrightFern IT solutions, a IT mananaged services company is looking to redesign current website (brightfernsolutions.example).

The website should convey professionalism within the managed it services community. The layout should invite users to explore other areas of the site. Should contain tools and other current information that clients or potential clients would find useful. Product pages, special offers and informational pages should be easily editable by non-programmers. Tidewarden.example is a good site to review as an example of the design components we like.

Target Market(s)

Professional services companies with 10-100 users

Industry/Entity Type

It Company

Requirements
Must have
• • Clickable icons and graphics are good
• SEO - Wordpress could be a great platform for us to work from as we already have internal experience with it and it’s easy to update. If not Wordpress, we would need something that is easy to SEO optimize
• An “our team” section with pictures
• Sell the message to potential clients why they need managed services
• Home page needs to convey our core services at a glance
• Home page needs to load quickly
• Screenshots of our monitoring and security reports
• Easy for us to update/edit certain areas
o New products
o Testimonials
Nice to have
• • Something like TW’s savings calculator - http://www.tidewarden.example/it-savings-calculator/
• Webform to enter service ticket requests
• Motion of home page banner
• Maybe pull in RSS feeds from current tech news sources
• Rotating content on all pages to keep it fresh
• “Fern-up” feature for monthly promos
Should not have
• • Should not be overly "techie" in feel.
• Not overly wordy (like current site)

```html
<!DOCTYPE html>
<html lang="en">
<head>
<meta charset="utf-8">
<title>BrightFern IT Solutions</title>
<link rel="stylesheet" href="https://fonts.googleapis.com/css2?family=Arimo:wght@400;700&display=swap">
<style>
:root{
  --green:#6cbd2a;
  --green-dark:#4f9a12;
  --green-light:#9be04a;
  --ink:#111;
  --muted:#777;
  --rule:#bbb;
  --nav:#111;
  --white:#fff;
  --sky-top:#1d5fc4;
  --sky-bottom:#7bb7ee;
}
*{box-sizing:border-box;margin:0;padding:0}
html,body{width:1041px;height:1200px;overflow:hidden;background:var(--white)}
body{position:relative;font-family:"Arimo",Arial,sans-serif;color:var(--ink)}
.abs{position:absolute}
a{color:inherit;text-decoration:none}

.brand{left:78px;top:30px;display:flex;align-items:center;gap:8px;color:var(--green);font-weight:700;font-size:22px}
.brand-dot{width:34px;height:34px;border-radius:50%;background:var(--green)}

.contact{right:65px;top:6px;text-align:right;font-size:12px;line-height:15px;color:var(--muted)}
.support{right:65px;top:48px;display:flex;align-items:center;gap:8px;font-size:13px;color:var(--green)}

.nav{left:496px;top:91px;display:flex;gap:4px;list-style:none}
.nav li{height:23px;line-height:23px;text-align:center;font-size:13px;color:var(--white);background:linear-gradient(#333,var(--nav));border-radius:6px}
.nav li.active{background:linear-gradient(var(--green-light),var(--green));color:var(--ink)}

.hero{left:52px;top:122px;width:941px;height:388px;background:linear-gradient(160deg,var(--sky-top),#3f86dc 55%,var(--sky-bottom))}
.hero-photo{left:0;top:0;width:470px;height:388px;background:linear-gradient(90deg,#c9a58f,#9fb6d6)}
.hero-title{left:585px;top:94px;font-size:37px;font-weight:700;color:var(--ink)}
.hero-text{left:585px;top:134px;width:320px;font-size:16px;line-height:21px;color:var(--white)}
.btn{left:685px;top:202px;width:78px;height:23px;line-height:23px;text-align:center;font-size:11px;border-radius:6px;background:linear-gradient(var(--green-light),var(--green));color:var(--ink)}

.sec-title{font-size:22px;font-weight:700;color:var(--green)}
.sec-title.plain{font-weight:400;color:var(--ink)}
.rule{height:1px;background:var(--rule)}
.copy{font-size:12.5px;line-height:17.3px;color:var(--ink)}
.more{font-size:11px;color:var(--green)}
.photo{display:block}

.team-photo{left:70px;top:574px;width:436px;height:141px;background:linear-gradient(#2050b8,#5ba0dc)}
.monitor-photo{left:540px;top:574px;width:434px;height:141px;background:linear-gradient(#3a3f48,#9aa1ab)}
.product{top:896px;width:144px;height:122px}
.p1{left:101px;background:linear-gradient(#fafafa,#cfcfcf)}
.p2{left:260px;background:linear-gradient(90deg,#3aa0e0,#f2b233 50%,#d64fb8)}
.p3{left:422px;background:radial-gradient(circle at 50% 55%,#b3202a,#111 70%)}
.arrow{top:945px}

.testi{left:643px;top:898px;width:332px;font-size:12px;line-height:17.5px}
.testi p{margin-bottom:18px}

.footer-nav{left:74px;top:1096px;display:flex;gap:23px;font-size:11px;list-style:none}
.footer-sub{left:74px;top:1122px;display:flex;gap:21px;font-size:9.5px;color:#444;list-style:none}
.calc{left:740px;top:1106px;display:flex;align-items:center;gap:10px;font-size:13px;color:var(--green)}
.legal{left:0;width:1041px;top:1177px;text-align:center;font-size:10px;color:#333}
</style>
</head>
<body>

<header>
  <div class="abs brand"><span class="brand-dot"></span>BrightFern</div>
  <div class="abs contact">Toll Free: (800) 555-0142<br>Phone: (555) 014-7720</div>
  <a class="abs support" href="#">
    <svg width="22" height="22" viewBox="0 0 22 22"><circle cx="11" cy="7" r="5" fill="#666"/><rect x="4" y="13" width="14" height="8" rx="2" fill="#999"/></svg>
    Remote Support
  </a>
  <ul class="abs nav">
    <li class="active" style="width:77px">Home</li>
    <li style="width:94px">Solutions</li>
    <li style="width:92px">Services</li>
    <li style="width:96px">About Us</li>
    <li style="width:104px">Contact Us</li>
  </ul>
</header>

<section class="abs hero">
  <div class="abs hero-photo" role="img" aria-label="Man touching a transparent touchscreen against a cloudy sky"></div>
  <h1 class="abs hero-title">BrightFern</h1>
  <p class="abs hero-text">can help your business harness the power of new technology, making your business fast and efficient.</p>
  <a class="abs btn" href="#">Read more</a>
</section>

<section>
  <svg class="abs" style="left:85px;top:535px" width="36" height="30" viewBox="0 0 36 30"><circle cx="14" cy="15" r="12" fill="#3b6fb8"/><circle cx="26" cy="20" r="7" fill="#999"/></svg>
  <h2 class="abs sec-title" style="left:125px;top:536px">Our Team</h2>
  <div class="abs rule" style="left:173px;top:564px;width:334px"></div>
  <div class="abs photo team-photo" role="img" aria-label="Hands of a diverse team holding up a globe"></div>
  <p class="abs copy" style="left:73px;top:729px;width:440px">Lorem Ipsum is simply dummy text of the printing and typesetting industry. Lorem Ipsum has been the industry's standard dummy text ever since the 1500s, when an unknown printer took a galley of type and scrambled it to make a type specimen book.</p>
  <a class="abs more" style="left:422px;top:812px" href="#">Read more</a>

  <svg class="abs" style="left:550px;top:535px" width="28" height="24" viewBox="0 0 28 24"><rect x="1" y="1" width="26" height="22" rx="3" fill="#445"/><rect x="5" y="5" width="18" height="14" fill="#3a8ee0"/></svg>
  <h2 class="abs sec-title" style="left:588px;top:534px">Monitoring &amp; Security Service</h2>
  <div class="abs rule" style="left:728px;top:564px;width:244px"></div>
  <div class="abs photo monitor-photo" role="img" aria-label="Network operations center with wall of monitors and staff at desks"></div>
  <p class="abs copy" style="left:541px;top:729px;width:440px">Lorem Ipsum is simply dummy text of the printing and typesetting industry. Lorem Ipsum has been the industry's standard dummy text ever since the 1500s, when an unknown printer took a galley of type and scrambled it to make a type specimen book.</p>
  <a class="abs more" style="left:905px;top:812px" href="#">Read more</a>
</section>

<section>
  <svg class="abs" style="left:73px;top:853px" width="26" height="28" viewBox="0 0 26 28"><circle cx="13" cy="14" r="12" fill="#eee" stroke="#ccc"/></svg>
  <h2 class="abs sec-title plain" style="left:110px;top:857px">New Products</h2>
  <div class="abs rule" style="left:175px;top:885px;width:390px"></div>
  <svg class="abs arrow" style="left:66px" width="24" height="24" viewBox="0 0 24 24"><circle cx="12" cy="12" r="12" fill="#ccc"/><path d="M17 12H7M11 7l-5 5 5 5" stroke="#fff" stroke-width="2.5" fill="none"/></svg>
  <div class="abs product p1" role="img" aria-label="Desktop computer tower with monitor and keyboard"></div>
  <div class="abs product p2" role="img" aria-label="Software product boxes"></div>
  <div class="abs product p3" role="img" aria-label="Laptop with red lit lid"></div>
  <svg class="abs arrow" style="left:576px" width="24" height="24" viewBox="0 0 24 24"><circle cx="12" cy="12" r="12" fill="#ccc"/><path d="M7 12h10M13 7l5 5-5 5" stroke="#fff" stroke-width="2.5" fill="none"/></svg>
  <a class="abs more" style="left:526px;top:1041px" href="#">View more</a>

  <svg class="abs" style="left:631px;top:852px" width="28" height="26" viewBox="0 0 28 26"><rect x="8" y="1" width="18" height="12" rx="3" fill="none" stroke="#c22" stroke-width="2"/><rect x="1" y="8" width="16" height="11" rx="3" fill="#fff" stroke="#2a5bb8" stroke-width="2"/><path d="M4 19l-1 5 5-5" fill="#2a5bb8"/></svg>
  <h2 class="abs sec-title plain" style="left:661px;top:857px">Testimonials</h2>
  <div class="abs rule" style="left:660px;top:885px;width:300px"></div>
  <div class="abs testi">
    <p><b>Lorem Ipsum</b> is simply dummy text of the printing and type-setting industry. Lorem Ipsum has been the industry's standard dummy text ever since the 1500s,</p>
    <p><b>Lorem Ipsum</b> is simply dummy text of the printing and type-setting industry. Lorem Ipsum has been the industry's standard dummy text ever since the 1500s,</p>
  </div>
  <a class="abs more" style="left:912px;top:1041px" href="#">Read more</a>
</section>

<footer>
  <div class="abs rule" style="left:55px;top:1081px;width:938px"></div>
  <ul class="abs footer-nav"><li>Home</li><li>Solutions</li><li>Services</li><li>About Us</li><li>Contact Us</li></ul>
  <ul class="abs footer-sub"><li>Careers</li><li>Sitemap</li></ul>
  <a class="abs calc" href="#">
    <svg width="19" height="24" viewBox="0 0 19 24"><rect x="0.5" y="0.5" width="18" height="23" rx="2" fill="#666"/><rect x="3" y="3" width="13" height="5" fill="#cde"/><g fill="#eee"><rect x="3" y="11" width="3" height="3"/><rect x="8" y="11" width="3" height="3"/><rect x="13" y="11" width="3" height="3"/><rect x="3" y="17" width="3" height="3"/><rect x="8" y="17" width="3" height="3"/><rect x="13" y="17" width="3" height="3"/></g></svg>
    Calculator for IT infrastructure
  </a>
  <div class="abs rule" style="left:55px;top:1155px;width:938px"></div>
  <p class="abs legal">All Rights Reserved, BrightFern 2012</p>
</footer>

</body>
</html>
```